Packaging design (small box) for Zelkor 5/6 cable (keychain cable)

we need a packaging to sell our cellphone cable.

1)I want the word "BRIX" on the life side in a stylish way...
2)The product must be mostly visible (not hidden with graphic or design)
3)Please design the sides of the packaging (colors,graphics,etc)
4)Please integrate my logo on the packaging (files 3) you can change the colour of the logo if you want.
Please check the attached files: The packaging will be exactly like this with the same material and size (file 2) (the design on the packaging of this picture is the degin by defaut from our supplier).

-They will be put in a counterdisplay

Size of the packaging:
W:36mm H:130mm D:17mm
We trust your creativity!

Attached files the sketch of our packaging and our products to inspire you.

Target Market(s)

16-35 male and female

Industry/Entity Type

Product

Requirements
Must have
• We need the following words on the packaging:
• 1)"Câble compatible pour Zelkor 5/6 " (on the front)
• 2) Recharge rapidement (meaning:charge fast)
• 3) Toujours à portée de la main ( meaning always with you)
• 4)BRIX on the left side
• 5)Our logo "Vantoro"
Nice to have
• I am really open about your ideas
Should not have

```html
<!DOCTYPE html>
<html lang="fr">
<head>
<meta charset="utf-8">
<title>Vantoro BRIX – dieline étui câble</title>
<link href="https://fonts.googleapis.com/css2?family=Roboto+Condensed:wght@400;500&family=Roboto:ital,wght@0,300;0,400;1,300;1,400&display=swap" rel="stylesheet">
<style>
  :root{
    --bg:#e9e9e9;
    --cut:#29b3e6;
    --paper:#ffffff;
    --ink:#231f20;
    --navy:#123e6e;
    --navy-mid:#1d5f9c;
    --blue:#3d8fcb;
    --sky:#6fb5df;
    --brand:#1d5f9c;
  }
  *{margin:0;padding:0;box-sizing:border-box}
  html,body{width:1105px;height:1200px;overflow:hidden;background:var(--bg)}
  .sheet{position:relative;width:1105px;height:1200px}
  .dieline{position:absolute;left:0;top:0;filter:drop-shadow(10px 10px 8px rgba(0,0,0,.28))}
  .txt{position:absolute;font-family:"Roboto Condensed",Arial,sans-serif}
  .brand-name{font-family:"Roboto Condensed",Arial,sans-serif;font-weight:500;color:var(--brand);font-size:13px;letter-spacing:1.5px}
  .brand-top{width:80px;text-align:center;top:310px}
  .product-title{font-size:35px;line-height:44px;color:var(--ink);font-weight:400;top:522px}
  .fast-charge{font-family:"Roboto",Arial,sans-serif;font-style:italic;font-weight:300;font-size:20px;line-height:27px;color:var(--navy);text-align:right;width:170px;top:722px}
  .always{font-size:29px;line-height:35px;color:#fff;font-weight:400;top:812px}
  .side-name{font-family:"Roboto",Arial,sans-serif;font-weight:300;font-size:74px;color:#fff;letter-spacing:4px;
    transform-origin:left top;transform:rotate(90deg);left:318px;top:298px;white-space:nowrap}
  .side-brand{transform-origin:left top;transform:rotate(90deg);left:252px;top:838px;white-space:nowrap;font-size:12px;color:var(--navy)}
  .side-claim{font-family:"Roboto",Arial,sans-serif;font-style:italic;font-weight:400;font-size:41px;color:#fff;letter-spacing:1px;
    transform-origin:left top;transform:rotate(-90deg);left:546px;top:838px;white-space:nowrap}
</style>
</head>
<body>
<main class="sheet">
  <svg class="dieline" width="1105" height="1200" viewBox="0 0 1105 1200" aria-hidden="false">
    <defs>
      <linearGradient id="sideFade" x1="0" y1="0" x2="0" y2="1">
        <stop offset="0" stop-color="#4a8fc8"/>
        <stop offset=".55" stop-color="#5aabdb"/>
        <stop offset=".82" stop-color="#a9d3ee"/>
        <stop offset="1" stop-color="#ffffff"/>
      </linearGradient>
      <radialGradient id="navyGlow" cx=".5" cy=".5" r=".7">
        <stop offset="0" stop-color="#1f7fc2"/>
        <stop offset="1" stop-color="var(--navy)"/>
      </radialGradient>
    </defs>

    <!-- flaps -->
    <g class="flaps" fill="var(--paper)" stroke="var(--cut)" stroke-width="1">
      <path d="M239 234 V170 L239 162 H304 L312 170 V234 Z"/>
      <path d="M239 957 V1022 L245 1030 H312 V965 Z"/>
      <path d="M532 234 V170 L532 162 H597 L605 170 V234 Z"/>
      <path d="M532 957 V1022 L538 1030 H605 V965 Z"/>
      <path d="M322 234 V118 Q322 106 334 106 H510 Q522 106 522 118 V234 Z"/>
      <path d="M322 957 V1073 Q322 1085 334 1085 H510 Q522 1085 522 1073 V957 Z"/>
      <path d="M616 234 V152 Q616 140 628 140 H804 Q816 140 816 152 V234 Z"/>
      <path d="M816 234 L878 242 V950 L816 957 Z"/>
    </g>
    <g class="folds" stroke="var(--cut)" stroke-width="1" fill="none">
      <path d="M322 150 H522 M363 150 l4 9 M481 150 l-4 9"/>
      <path d="M322 1040 H522 M363 1040 l4 -9 M481 1040 l-4 -9"/>
    </g>
    <path class="hang-hole" d="M680 180 H700 Q704 168 716 168 Q728 168 732 180 H752 Q762 180 762 192 Q762 205 752 205 H680 Q670 205 670 192 Q670 180 680 180 Z" fill="var(--bg)" stroke="var(--cut)"/>

    <!-- side panels -->
    <g role="img" aria-label="Abstract flowing blue wave graphic on the left side panel">
      <rect x="227" y="234" width="95" height="723" fill="url(#sideFade)"/>
      <rect x="227" y="234" width="95" height="6" fill="#1a6fad"/>
    </g>
    <g role="img" aria-label="Abstract flowing blue wave graphic on the right side panel">
      <rect x="522" y="234" width="94" height="723" fill="url(#sideFade)"/>
      <rect x="522" y="234" width="94" height="6" fill="#1a6fad"/>
    </g>

    <!-- front & back panels -->
    <g class="faces" stroke="var(--cut)" stroke-width="1">
      <rect x="322" y="234" width="200" height="723" fill="var(--paper)"/>
      <rect x="616" y="234" width="200" height="723" fill="var(--paper)"/>
    </g>
    <g class="claim-boxes">
      <rect x="324" y="705" width="196" height="82" fill="#fff" stroke="var(--navy)" stroke-width="3"/>
      <rect x="322" y="786" width="200" height="171" fill="url(#navyGlow)"/>
      <rect x="618" y="705" width="196" height="82" fill="#fff" stroke="var(--navy)" stroke-width="3"/>
      <rect x="616" y="786" width="200" height="171" fill="url(#navyGlow)"/>
    </g>
    <rect x="227" y="234" width="651" height="723" fill="none" stroke="var(--cut)" stroke-width="1"/>
    <path d="M322 234 V957 M522 234 V957 M616 234 V957 M816 234 V957" stroke="var(--cut)" fill="none"/>

    <!-- brand circles -->
    <g class="brand-mark" fill="var(--brand)">
      <circle cx="466" cy="280" r="26"/>
      <circle cx="760" cy="280" r="26"/>
      <circle cx="282" cy="880" r="26"/>
    </g>

    <!-- fast charge icons -->
    <g class="charge-icon">
      <circle cx="362" cy="734" r="15" fill="var(--navy)"/>
      <rect x="353" y="728" width="16" height="11" rx="1.5" fill="none" stroke="#fff" stroke-width="1.6"/>
      <rect x="369" y="731" width="2" height="5" fill="#fff"/>
      <path d="M362 726 L357 735 H362 L360 742 L367 732 H362 Z" fill="#fff"/>
      <circle cx="656" cy="734" r="15" fill="var(--navy)"/>
      <rect x="647" y="728" width="16" height="11" rx="1.5" fill="none" stroke="#fff" stroke-width="1.6"/>
      <rect x="663" y="731" width="2" height="5" fill="#fff"/>
      <path d="M656 726 L651 735 H656 L654 742 L661 732 H656 Z" fill="#fff"/>
    </g>
    <g class="battery-icon">
      <circle cx="569" cy="884" r="32" fill="var(--navy)" stroke="#fff" stroke-width="2"/>
      <rect x="559" y="866" width="20" height="34" rx="2" fill="none" stroke="#fff" stroke-width="3"/>
      <rect x="565" y="861" width="8" height="5" fill="#fff"/>
      <path d="M572 870 L562 886 H569 L566 898 L577 881 H570 Z" fill="#fff"/>
    </g>
  </svg>

  <!-- left side -->
  <div class="txt side-name">BRIX</div>
  <div class="txt brand-name side-brand">VANTORO</div>

  <!-- front -->
  <div class="txt brand-name brand-top" style="left:426px">VANTORO</div>
  <h1 class="txt product-title" style="left:343px">Câble<br>compatible<br>pour<br>Zelkor 5/6</h1>
  <p class="txt fast-charge" style="left:324px">RECHARGE<br>RAPIDEMENT</p>
  <p class="txt always" style="left:351px">TOUJOURS<br>À PORTÉE<br>DE LA MAIN</p>

  <!-- right side -->
  <div class="txt side-claim">RECHARGE&nbsp; RAPIDEMENT</div>

  <!-- back -->
  <div class="txt brand-name brand-top" style="left:720px">VANTORO</div>
  <h2 class="txt product-title" style="left:637px">Câble<br>compatible<br>pour<br>Zelkor 5/6</h2>
  <p class="txt fast-charge" style="left:618px">RECHARGE<br>RAPIDEMENT</p>
  <p class="txt always" style="left:645px">TOUJOURS<br>À PORTÉE<br>DE LA MAIN</p>
</main>
</body>
</html>
```